Luxury and organic beauty products need a Design

We need a bottle and packaging design for a new business in New Zealand, called Keravi Botanicals. We are creating a selection of Luxury and premium products to have at the Keravi luxury villa's (www.keraviluxuryvilla.com), as well to sell online and at boutique stores.

The products are: Body wash, Shampoo, Conditioner, Hand wash, Body lotion, Air fresheners and Bath salts.

We would like to use the Keravi Botanicals logo in Silver as Keravi Luxury Villa's a having it in Gold, so it separates the two products. Also the packaging will be Navy Blue along with the silver.

The final design should be sleek, sophisticated and have a luxury feel. Our customers will have the product in the bathroom and kitchen so the bottles must be proud to show off. " This should look and feel like a very high end product.

Boxes will have embossed writing (logo) and a slightly textured feel or look.

Please find attached images of some examples to use for inspiration only.

Target Market(s)

Luxury boutique villas, Boutique stores, High end stores

Industry/Entity Type

Personal and hair care

Colors
0054AA
0677BA
7BADD7
CADEEF
E8F1F8
FFC000
F8CF3A
FAE287
FDF2CF
FEFAEE

Requirements
Must have
• Use the provided Logo, look and feel luxurious, but at the same time organic
Nice to have
• A bottle that reminds precious stones. I have just attached an example
Should not have
• Dark colour, heavy fonts

```html
<!DOCTYPE html>
<html lang="en">
<head>
<meta charset="utf-8">
<title>Keravi Botanicals – Bath Collection Packaging</title>
<link rel="stylesheet" href="https://fonts.googleapis.com/css2?family=Lato:wght@400&display=swap">
<style>
  :root {
    --navy-deep: #0b1a36;
    --navy: #14284f;
    --navy-ink: #0f2149;
    --silver-edge: #8c8f94;
    --silver-mid: #b9bcc1;
    --silver-light: #e4e6e9;
    --silver-shine: #f4f5f6;
    --groove-dark: #5b5f66;
    --lotus-tone: rgba(70, 76, 88, 0.35);
  }
  * { margin: 0; padding: 0; box-sizing: border-box; }
  html, body { width: 1200px; height: 736px; overflow: hidden; }
  body {
    position: relative;
    background: radial-gradient(ellipse 70% 60% at 50% 62%, var(--navy) 0%, var(--navy-deep) 100%);
    font-family: "Lato", sans-serif;
    color: var(--navy-ink);
  }

  .container {
    position: absolute;
    border-radius: 8px 8px 4px 4px;
    background: linear-gradient(90deg,
      var(--silver-edge) 0%,
      var(--silver-mid) 14%,
      var(--silver-light) 38%,
      var(--silver-shine) 48%,
      var(--silver-mid) 76%,
      var(--silver-edge) 100%);
    box-shadow: 0 18px 30px rgba(0, 0, 0, 0.35);
  }
  .container__groove {
    position: absolute;
    left: -2px; right: -2px;
    border-radius: 8px;
    background: linear-gradient(180deg,
      var(--silver-shine) 0%,
      var(--silver-mid) 35%,
      var(--groove-dark) 60%,
      var(--silver-light) 100%);
  }
  .brand-mark {
    position: absolute;
    left: 50%;
    transform: translateX(-50%);
    border-radius: 50%;
    background: var(--navy-ink);
  }
  .brand-name {
    position: absolute;
    left: 0; right: 0;
    text-align: center;
    font-weight: 400;
    text-transform: uppercase;
    line-height: 1;
    color: var(--navy-ink);
  }
  .brand-name--main { letter-spacing: 0.06em; }
  .brand-name--sub { letter-spacing: 0.32em; }
  .product-name {
    position: absolute;
    left: 0; right: 0;
    text-align: center;
    font-weight: 400;
    line-height: 1;
    letter-spacing: 0.02em;
    color: var(--navy-ink);
  }
  .lotus-art {
    position: absolute;
    background: radial-gradient(ellipse 55% 55% at 50% 55%, var(--lotus-tone) 0%, rgba(70, 76, 88, 0) 100%);
  }

  /* Shampoo bottle */
  .container--shampoo { left: 534px; top: 95px; width: 153px; height: 493px; }
  .container--shampoo .container__groove { top: 174px; height: 14px; }
  .container--shampoo .brand-mark { top: 50px; width: 44px; height: 44px; }
  .container--shampoo .brand-name--main { top: 104px; font-size: 19px; }
  .container--shampoo .brand-name--sub { top: 130px; font-size: 7px; }
  .container--shampoo .product-name { top: 226px; font-size: 17px; }
  .container--shampoo .lotus-art { left: 11px; top: 258px; width: 104px; height: 232px; }

  /* Bath salt jar */
  .container--bath-salt { left: 301px; top: 403px; width: 207px; height: 185px; }
  .container--bath-salt .container__groove { top: 62px; height: 14px; }
  .container--bath-salt .brand-mark { top: 106px; width: 24px; height: 24px; }
  .container--bath-salt .brand-name--main { top: 137px; font-size: 11px; }
  .container--bath-salt .brand-name--sub { top: 150px; font-size: 5px; }
  .container--bath-salt .product-name { top: 160px; font-size: 14px; }
  .container--bath-salt .lotus-art { left: 152px; top: 94px; width: 54px; height: 88px; }

  /* Air freshener jar */
  .container--air-freshener { left: 636px; top: 370px; width: 255px; height: 259px; }
  .container--air-freshener .container__groove { top: 76px; height: 16px; }
  .container--air-freshener .brand-mark { top: 128px; width: 34px; height: 34px; }
  .container--air-freshener .brand-name--main { top: 176px; font-size: 14px; }
  .container--air-freshener .brand-name--sub { top: 194px; font-size: 6px; }
  .container--air-freshener .product-name { top: 214px; font-size: 16px; }
  .container--air-freshener .lotus-art { left: 192px; top: 110px; width: 62px; height: 146px; }
</style>
</head>
<body>
  <section class="container container--bath-salt">
    <div class="container__groove"></div>
    <span class="brand-mark"></span>
    <p class="brand-name brand-name--main">Keravi</p>
    <p class="brand-name brand-name--sub">Botanicals</p>
    <p class="product-name">Bath Salt</p>
    <div class="lotus-art" role="img" aria-label="Line illustration of lotus flowers and leaves"></div>
  </section>

  <section class="container container--shampoo">
    <div class="container__groove"></div>
    <span class="brand-mark"></span>
    <p class="brand-name brand-name--main">Keravi</p>
    <p class="brand-name brand-name--sub">Botanicals</p>
    <p class="product-name">Shampoo</p>
    <div class="lotus-art" role="img" aria-label="Line illustration of tall lotus flowers, buds and leaves"></div>
  </section>

  <section class="container container--air-freshener">
    <div class="container__groove"></div>
    <span class="brand-mark"></span>
    <p class="brand-name brand-name--main">Keravi</p>
    <p class="brand-name brand-name--sub">Botanicals</p>
    <p class="product-name">Air Freshener</p>
    <div class="lotus-art" role="img" aria-label="Line illustration of lotus flowers and leaves"></div>
  </section>
</body>
</html>
```